Powerpoint visual improvements

I need a cover page, and our beliefs page and differentiating factors page / graphic design for our presentation. For the cover page I would just like an attractive design that incorporate our architectural concept with columns and potentially our logo. For the beliefs page I just want a more attractive presentatoin of the concepts. For the differentiating factors page I want a graphic that captures the points about how we are different from competitors. I have used the attached content to date, but I think it can be improved. The text is included in the graphic and I would also like to make sure the firm logo is incorporated.

Target Market(s)

Individual and institutional investors.

Industry/Entity Type

Investment Advisory

Requirements
Must have
• Our corporate colors are generally RGB 145,148,149; 66,68,76; 0,0,153; and 0,63,127. Our logo is attached. Our primary font is Georgia. Our website is www.PelmarCW.com. The key pages are www.PelmarCW.com/beliefs and www.PelmarCW.com/value we are trying to capture in a presentation. We also need a new presentation cover. Use the website as a reference for the type of imagery we like.

```html
<!DOCTYPE html>
<html lang="en">
<head>
<meta charset="UTF-8">
<title>The Pelmar Difference</title>
<link rel="stylesheet" href="https://fonts.googleapis.com/css2?family=Gelasio:wght@400;700&display=swap">
<style>
  :root {
    --brand-navy: #003f7f;
    --brand-charcoal: #42444c;
    --ink: #111111;
    --paper: #ffffff;
  }
  * { margin: 0; padding: 0; box-sizing: border-box; }
  html, body { width: 1200px; height: 675px; overflow: hidden; background: var(--paper); }
  .slide {
    position: relative;
    width: 1200px;
    height: 675px;
    background: var(--paper);
    font-family: "Gelasio", Georgia, serif;
    overflow: hidden;
  }
  .title-band {
    position: absolute;
    left: 0; top: 0;
    width: 1200px; height: 82px;
    background: var(--brand-navy);
  }
  .slide-title {
    position: absolute;
    left: 450px; width: 708px; top: 10px;
    text-align: center;
    color: var(--paper);
    font-weight: 400;
    font-size: 55px;
    line-height: 62px;
    white-space: nowrap;
  }
  .brand-tab {
    position: absolute;
    left: 0; top: 33px;
    width: 445px; height: 113px;
    background: var(--brand-charcoal);
    clip-path: polygon(0 0, 445px 0, 354px 113px, 0 113px);
  }
  .brand-name {
    position: absolute;
    left: 94px; top: 26px;
    display: flex;
    align-items: center;
    gap: 10px;
    color: var(--paper);
    font-weight: 400;
  }
  .brand-mark {
    width: 42px; height: 42px;
    border-radius: 50%;
    background: var(--paper);
    flex: none;
  }
  .brand-words { display: flex; flex-direction: column; line-height: 1; }
  .brand-words .primary { font-size: 32px; }
  .brand-words .secondary { font-size: 10px; letter-spacing: 0.5px; margin-top: 5px; text-transform: uppercase; }
  .feature-icon {
    position: absolute;
    left: 196px; top: 302px;
    width: 196px; height: 186px;
  }
  .feature {
    position: absolute;
    left: 452px; top: 266px;
    width: 520px;
  }
  .feature-heading {
    color: var(--brand-navy);
    font-weight: 700;
    font-size: 25px;
    line-height: 34px;
    margin-bottom: 30px;
  }
  .feature-body {
    color: var(--ink);
    font-weight: 700;
    font-size: 15.6px;
    line-height: 45px;
    white-space: nowrap;
  }
  .footer-band {
    position: absolute;
    left: 0; bottom: 0;
    width: 1200px; height: 14px;
    background: var(--brand-navy);
  }
</style>
</head>
<body>
<main class="slide">
  <div class="title-band"></div>
  <h1 class="slide-title">The Pelmar Difference</h1>

  <div class="brand-tab">
    <div class="brand-name">
      <span class="brand-mark"></span>
      <span class="brand-words">
        <span class="primary">Pelmar</span>
        <span class="secondary">Capital Wealth</span>
      </span>
    </div>
  </div>

  <svg class="feature-icon" viewBox="0 0 196 186" aria-hidden="true">
    <g fill="none" stroke="#000" stroke-width="11" stroke-linecap="round" stroke-linejoin="round">
      <path d="M64 30 V18 a10 10 0 0 1 10 -10 H122 a10 10 0 0 1 10 10 V30"/>
      <rect x="6" y="32" width="184" height="146" rx="18"/>
      <path d="M6 92 H190"/>
      <path d="M62 80 V104"/>
      <path d="M134 80 V104"/>
    </g>
  </svg>

  <section class="feature">
    <h2 class="feature-heading">Experience</h2>
    <p class="feature-body">We are investors with a passion for investing. Each of our<br>founders is a chartered analyst and collectively our team has<br>decades of experience in investment analysis, portfolio<br>construction, due diligence, research and security valuation.</p>
  </section>

  <div class="footer-band"></div>
</main>
</body>
</html>
```